3 Medical Provider Brochures targeted at doctors and patients

We are a diagnostic imaging provider.

We need 3 brochure layouts.

1) A 4-fold with our 4 locations...one on each panel
2) A single-sheet brochure marketing each of our procedures to the referring physicians. (a shell, one completed so we clone the rest)
3) A single-sheet brochure handout containing information about certain exams and ways to prepare for our patients' education. (a shell, one completed so we can clone the rest)

Target Market(s)

4-fold target is for the referral coordinator in a doctors office, so they can find our location at-a-glance
One of the single broadsheets to the referring physician marketing a particular modality (CAT Scan, MRI, X-ray, Ultrasound, Mammography, Breast Biopsy)
The other single Broadsheet is marketed to patients but handed out by doctors who want to send patients to be scanned at our facility.

Industry/Entity Type

Medical Imaging

Font styles to use
Sans Serif

Colors
3276b5
0255a3
85cae6
ffffff

Requirements
Must have
• The 4-fold should be easy to read at-a-glance but contain some branding.
• The doctor-facing broadsheet should be in a the form of a shell, so we can do one for each of our modalities
• The patient-facing should be a shell as well, so we can do one for each of our major exams.
• Our name is KEL MRI and Imaging Centers. KEL means Kind Every Lane. KEL IS Kind Every Lane.
Nice to have
• Friendly faces, but professional and knowledgeable.
• Easy-to-update brochure shell contents

```html
<!DOCTYPE html>
<html lang="en">
<head>
<meta charset="utf-8">
<title>KEL MRI &amp; Imaging Centers – Locations</title>
<link rel="stylesheet" href="https://fonts.googleapis.com/css2?family=Bebas+Neue&family=Lato:wght@300;400;700;900&display=swap">
<style>
  :root {
    --blue-deep: #0a78cc;
    --blue-deep-2: #0255a3;
    --blue-bright: #0fa8e6;
    --blue-soft: #85cae6;
    --white: #ffffff;
    --ink: #111111;
    --grey: #737373;
  }
  * { margin: 0; padding: 0; box-sizing: border-box; }
  html, body { width: 1200px; height: 737px; overflow: hidden; background: #ffffff; }
  .brochure {
    display: flex;
    width: 1200px;
    height: 737px;
    font-family: "Lato", Arial, sans-serif;
    color: var(--ink);
  }
  .panel {
    position: relative;
    width: 300px;
    height: 737px;
    display: flex;
    flex-direction: column;
    align-items: center;
    text-align: center;
  }
  .panel--deep { background: linear-gradient(180deg, var(--blue-deep) 0%, #0b86d6 100%); color: var(--white); }
  .panel--white { background: var(--white); }
  .panel--bright { background: var(--blue-bright); color: var(--white); }

  .location-title {
    font-family: "Bebas Neue", "Arial Narrow", sans-serif;
    font-weight: 400;
    font-size: 38px;
    line-height: 0.92;
    letter-spacing: 0.3px;
  }
  .address { font-size: 13px; line-height: 17px; font-weight: 400; margin-top: 14px; }
  .contact { font-size: 13px; line-height: 17px; font-weight: 700; margin-top: 12px; letter-spacing: 0.3px; }
  .services { font-size: 13.5px; line-height: 17px; margin-top: 18px; }
  .services strong { font-weight: 700; }
  .staff-label { font-size: 12.5px; line-height: 16px; margin-top: 20px; }
  .staff-name { font-size: 15px; line-height: 19px; font-weight: 700; letter-spacing: 0.2px; }
  .staff-name small { font-size: 12.5px; font-weight: 400; }
  .staff-and { font-size: 12.5px; line-height: 16px; }
  .muted { color: var(--grey); }

  .photo {
    width: 244px;
    height: 244px;
    border-radius: 50%;
    flex-shrink: 0;
  }
  .photo--team-blue { background: radial-gradient(circle at 50% 40%, #ffffff 0%, #e8eef4 55%, #b9c9da 100%); }
  .photo--team-white { background: radial-gradient(circle at 50% 45%, #f6f6f6 0%, #e3e6e8 55%, #c5ccd2 100%); }
  .photo--scan { background: radial-gradient(circle at 55% 45%, #5c86a8 0%, #2c4f6e 55%, #142a40 100%); }
  .photo--patient { background: radial-gradient(circle at 45% 45%, #f1ebe6 0%, #c9cfd5 55%, #8f9aa5 100%); }

  .panel--boca { padding-top: 88px; }
  .panel--boca .photo { position: absolute; top: 468px; left: 28px; }
  .panel--boca .services { font-size: 14.5px; line-height: 19px; margin-top: 26px; }

  .panel--cooper { padding-top: 42px; }
  .panel--cooper .location-title { margin-top: 30px; }

  .panel--coral { padding-top: 56px; }
  .panel--coral .location-title { font-size: 33px; line-height: 1.12; }
  .panel--coral .address { margin-top: 8px; }
  .panel--coral .photo { position: absolute; top: 348px; left: 28px; }

  .brand {
    position: absolute;
    top: 620px;
    left: 0;
    width: 300px;
    color: var(--white);
    font-family: "Lato", Arial, sans-serif;
    font-weight: 700;
    text-align: center;
  }
  .brand__name { display: block; font-size: 46px; line-height: 46px; letter-spacing: 1px; }
  .brand__sub { display: block; font-size: 15px; line-height: 20px; letter-spacing: 2px; margin-top: 4px; }

  .panel--plantation { padding-top: 42px; }
  .panel--plantation .location-title { margin-top: 38px; }
</style>
</head>
<body>
<main class="brochure">

  <section class="panel panel--deep panel--boca">
    <h2 class="location-title">Boca<br>Location</h2>
    <p class="address">1450 Harbor Palm Way<br>Suite 120<br>Boca Raton, FL 33431</p>
    <p class="contact">Tel: 561.555.0126<br>Fax: 561.555.0167</p>
    <p class="services"><strong>Provides</strong> High-field MRI,<br>Ultrasound X-ray and Mammography</p>
    <p class="staff-label">Your Marketing Associate is</p>
    <p class="staff-name">Marco Delgado, 555-555-5555</p>
    <p class="staff-label">Your Facility Manager is</p>
    <p class="staff-name">Tara Whitlock, 561-555-0126</p>
    <div class="photo photo--team-blue" role="img" aria-label="Photo of a friendly medical team in white coats and scrubs"></div>
  </section>

  <section class="panel panel--white panel--cooper">
    <div class="photo photo--team-white" role="img" aria-label="Photo of a smiling senior doctor with clipboard and colleagues"></div>
    <h2 class="location-title">Cooper City<br>Location</h2>
    <p class="address">8820 Lantern Bay Road<br>Suite 101<br>Cooper City, FL 33026</p>
    <p class="contact">Tel: 954.555.7466<br>Fax: 954.555.7489</p>
    <p class="services"><strong>Provides</strong> High-field MRI, Helical CT,<br>Ultrasound, X-ray, DEXA, Breast Biopsy<br>and Mammography</p>
    <p class="staff-label muted">Your Marketing Associates are</p>
    <p class="staff-name muted">Lena Castillo, 555-555-5555</p>
    <p class="staff-name muted"><small>and</small> Owen Mercer, 555-555-5555</p>
    <p class="staff-label muted">Your Facility Manager is</p>
    <p class="staff-name muted">Hannah Reyes, 954-555-7466</p>
  </section>

  <section class="panel panel--bright panel--coral">
    <h2 class="location-title">Coral Springs/Margate<br>Location</h2>
    <p class="address">2800 N. Cypress Road,<br>Suite 103<br>Margate FL 33063</p>
    <p class="contact" style="color: var(--ink);">Tel: 954-555-2020<br>Fax: 954-555-1855</p>
    <p class="services"><strong>Provides</strong> Ultra High Field 3.0T MRI</p>
    <p class="staff-label" style="color: var(--ink);">Your Marketing Associate is</p>
    <p class="staff-name" style="color: var(--ink);">Paula Benedetti, 555-555-5555</p>
    <div class="photo photo--scan" role="img" aria-label="Photo of a surgeon reviewing a digital X-ray scan display"></div>
    <p class="brand">
      <span class="brand__name">KEL MRI</span>
      <span class="brand__sub">&amp; IMAGING CENTERS</span>
    </p>
  </section>

  <section class="panel panel--white panel--plantation">
    <div class="photo photo--patient" role="img" aria-label="Photo of a smiling patient surrounded by gloved hands holding imaging tools"></div>
    <h2 class="location-title">Plantation<br>Location</h2>
    <p class="address">5120 West Orchid Blvd.<br>Plantation, Florida 33313</p>
    <p class="contact">Tel: 954.555.0551<br>Fax: 954.555.1856</p>
    <p class="services"><strong>Provides</strong> High-field MRI, Open MRI,<br>Helical CT, Ultrasound, X-ray, DEXA,<br>Breast Biopsy and Mammography</p>
    <p class="staff-label">Your marketing associates are</p>
    <p class="staff-name">Rosalind Medina, 555-555-5555</p>
    <p class="staff-and">and</p>
    <p class="staff-name">Clara Nolan, 555-555-5555</p>
    <p class="staff-label">Your Facility Manager is</p>
    <p class="staff-name">Iris Bellamy, 555-555-5555</p>
  </section>

</main>
</body>
</html>
```